Wedding dance company needs flyer design

I am looking for a double sided A5 flyer to be designed for my company Step Quill.

The concept of the flyer is to attract couples for their first wedding dance.

This is to support content of our website: http://www.stepquillgroup.example/bridal-set

All the text content for the flyer is attached in flyer.txt. My company logo is attached in logo.zip.

I would like to have 1-2 photos on the flyer based on a couple and their wedding first dance and perhaps some designs without photos (graphics instead).

```html
<!DOCTYPE html>
<html lang="en">
<head>
<meta charset="utf-8">
<title>Step Quill – First Dance Flyer</title>
<link rel="stylesheet" href="https://fonts.googleapis.com/css2?family=Bebas+Neue&family=Lato:ital,wght@0,400;0,700;0,900;1,700&family=Caveat:wght@600&display=swap">
<style>
  :root {
    --pink: #ec2a8e;
    --lime: #b7d433;
    --lime-light: #d4ea6a;
    --charcoal: #3a3a3d;
    --charcoal-dark: #2b2b2e;
    --ink: #1f1f22;
    --white: #ffffff;
    --photo-light: #d9d2c4;
    --photo-mid: #a5a58a;
    --photo-dark: #4a4a44;
  }
  * { box-sizing: border-box; margin: 0; padding: 0; }
  html, body { width: 904px; height: 1200px; overflow: hidden; background: var(--white); }
  .flyer {
    position: relative;
    width: 904px;
    height: 1200px;
    overflow: hidden;
    font-family: 'Lato', sans-serif;
    background: var(--charcoal);
  }
  .hero-photo {
    position: absolute;
    left: 0; top: 0;
    width: 904px; height: 580px;
    background: linear-gradient(115deg, var(--photo-mid) 0%, var(--photo-light) 38%, #eeeae2 60%, var(--photo-dark) 100%);
  }
  .brand-band {
    position: absolute;
    left: 0; top: 0;
    width: 560px; height: 220px;
    background: linear-gradient(180deg, rgba(40,40,42,0.92) 0%, rgba(40,40,42,0.75) 60%, rgba(40,40,42,0) 100%);
  }
  .brand {
    position: absolute;
    left: 36px; top: 52px;
    display: flex; align-items: center; gap: 16px;
  }
  .brand-dot {
    width: 24px; height: 24px; border-radius: 50%;
    background: var(--pink);
  }
  .brand-name {
    font-weight: 900;
    font-size: 74px;
    line-height: 1;
    color: var(--pink);
  }
  .waves { position: absolute; left: 0; top: 0; }
  .headline {
    position: absolute;
    left: 29px; top: 234px;
  }
  .headline-lead {
    font-family: 'Bebas Neue', sans-serif;
    font-size: 40px;
    color: var(--charcoal-dark);
    line-height: 1;
  }
  .headline-main {
    font-weight: 900;
    font-size: 50px;
    line-height: 58px;
    color: var(--pink);
    margin-top: 8px;
  }
  .starburst { position: absolute; left: 540px; top: 318px; }
  .starburst-text {
    position: absolute;
    left: 578px; top: 381px;
    width: 280px;
    text-align: center;
    font-family: 'Bebas Neue', sans-serif;
    font-size: 31px;
    line-height: 41px;
    color: var(--white);
  }
  .script {
    font-family: 'Caveat', cursive;
    font-weight: 600;
    color: var(--lime);
  }
  .planning-line {
    position: absolute;
    left: 120px; top: 470px;
    width: 410px;
    text-align: center;
    font-size: 35px;
    line-height: 48px;
  }
  .packages {
    position: absolute;
    left: 0; top: 573px;
    width: 470px; height: 151px;
    background: var(--pink);
    border-radius: 0 14px 14px 0;
    padding: 5px 14px 0 16px;
    color: var(--white);
    font-size: 17px;
    line-height: 24px;
  }
  .packages .tier {
    font-family: 'Caveat', cursive;
    font-weight: 600;
    font-size: 19px;
    color: var(--lime-light);
  }
  .extras {
    position: absolute;
    left: 0; top: 724px;
    width: 487px; height: 86px;
    background: var(--lime);
    border-radius: 0 0 14px 0;
    border-bottom: 5px solid var(--pink);
    padding: 3px 40px 0 20px;
    font-size: 17px;
    font-weight: 700;
    font-style: italic;
    line-height: 24px;
    color: var(--ink);
  }
  .about {
    position: absolute;
    right: 20px; top: 652px;
    width: 310px;
    text-align: right;
    font-size: 17px;
    line-height: 24px;
    color: var(--white);
  }
  .intro {
    position: absolute;
    left: 14px; top: 818px;
    width: 876px;
    font-size: 13px;
    line-height: 18px;
    color: var(--white);
  }
  .bespoke-line {
    position: absolute;
    left: 40px; top: 854px;
    width: 824px;
    text-align: center;
    font-size: 31px;
    line-height: 38px;
  }
  .contact {
    position: absolute;
    left: 0; top: 1016px;
    width: 904px;
    text-align: center;
    font-style: normal;
    font-weight: 700;
    font-size: 20px;
    line-height: 28px;
    color: var(--ink);
  }
  .web-tab {
    position: absolute;
    left: 149px; top: 1140px;
    width: 608px; height: 60px;
    background: var(--pink);
    border-radius: 14px 14px 0 0;
    text-align: center;
    font-weight: 700;
    font-size: 32px;
    line-height: 62px;
    color: var(--ink);
  }
</style>
</head>
<body>
<main class="flyer">
  <div class="hero-photo" role="img" aria-label="Photo of a bride and groom sharing their first dance outdoors"></div>
  <div class="brand-band"></div>
  <div class="brand">
    <span class="brand-dot"></span>
    <span class="brand-name">Step Quill</span>
  </div>

  <svg class="waves" width="904" height="1200" viewBox="0 0 904 1200" aria-hidden="true">
    <defs>
      <linearGradient id="lime-field" x1="0" y1="0" x2="0" y2="1">
        <stop offset="0" stop-color="#c6e04a"/>
        <stop offset="1" stop-color="#a9c92a"/>
      </linearGradient>
    </defs>
    <path d="M0,446 C300,400 620,430 904,505 L904,1200 L0,1200 Z" fill="#ffffff"/>
    <path d="M0,460 C300,416 620,446 904,520 L904,1200 L0,1200 Z" fill="var(--pink)"/>
    <path d="M0,480 C300,438 620,466 904,540 L904,1200 L0,1200 Z" fill="var(--lime)"/>
    <path d="M0,502 C300,464 620,490 904,562 L904,1200 L0,1200 Z" fill="var(--charcoal)"/>
    <path d="M0,932 C300,960 600,980 904,952 L904,1200 L0,1200 Z" fill="var(--pink)"/>
    <path d="M0,946 C300,976 600,996 904,968 L904,1200 L0,1200 Z" fill="#ffffff"/>
    <path d="M0,956 C300,986 600,1006 904,978 L904,1200 L0,1200 Z" fill="url(#lime-field)"/>
  </svg>

  <div class="headline">
    <p class="headline-lead">ARE YOU FEELING NERVOUS</p>
    <p class="headline-main">ABOUT YOUR<br>FIRST DANCE?</p>
  </div>

  <p class="planning-line script">Step Quill take care of all<br>the planning for you!</p>

  <svg class="starburst" width="356" height="310" viewBox="0 0 356 310" aria-hidden="true">
    <polygon fill="var(--pink)" stroke="#ffffff" stroke-width="7" stroke-linejoin="round"
      points="178,8 200,42 236,18 244,58 288,46 282,86 330,90 308,124 350,146 312,168 342,204 298,212 310,254 266,248 260,292 222,268 196,302 178,266 152,302 132,266 94,292 90,250 44,256 58,214 14,206 44,170 6,148 48,126 26,92 72,88 68,48 110,58 120,18 156,42"/>
  </svg>
  <p class="starburst-text">WE PROVIDE A WIDE<br>RANGE OF DANCE STYLES<br>AND VARIOUS PACKAGES<br>TO SUIT ALL BUDGETS</p>

  <section class="packages">
    <p><span class="tier">Packages</span> (starting at £65)</p>
    <p><span class="tier">Bronze Package ~</span> 1 x 1 hour lesson</p>
    <p><span class="tier">Silver Package ~</span> 1 x 90 minute lesson</p>
    <p><span class="tier">Gold Package ~</span> 2 x 90 minute lessons</p>
    <p><span class="tier">Platinum Package ~</span> 1 x 2 hour lesson and 2 x 90<br>minute lessons</p>
  </section>
  <p class="extras">We also offer the SOS last minute package, on-site rehearsals, hen parties and gift vouchers.</p>

  <p class="about">Step Quill specialise in preparing couples for their first dance to ensure it’s memorable. Lessons can take place in a studio of your choice or in the comfort of your own home.</p>

  <p class="intro">Step Quill, a small family business, provide flexibility and personal touches to make you feel comfortable and confident on the dance floor. Whether you want simple steps, a classic Waltz or a glitzy extravaganza, you'll soon be able to wow your friends and family.</p>

  <p class="bespoke-line script">Your bespoke first wedding dance will match your song, natural style<br>and ability, so it will never be too difficult and will suit you perfectly</p>

  <address class="contact">
    <p>Tel- 07700900118 / 07700900119</p>
    <p>Email- info@stepquillgroup.example</p>
    <p>Chatter - @StepQuillCo</p>
    <p>Friendbook- friendbook.example/stepquillgroupevents</p>
  </address>

  <p class="web-tab">www.stepquillgroup.example</p>
</main>
</body>
</html>
```